Tumble Tap Weekly Special Flyer

Looking for a professional weekly special promotion flyer to handout. Something I can edit and use as specials change. We are a small bar in a rural town (country). Something that can be use everyday software

Tumble Tap
518 Birchgrove Lane
Wellington, Ohio 57129
(555) 318-9047
Join Us on Pagewave \Tumbletap

$1.00 Domestic Drafts every day during happy hour
Happy hour hours = Mon-Fri 3-7 Sat & Sun 12-7

Sundays:
Free Pool ALL day on both tables
$1.00 Domestic drafts until midnight

$3.00 Appetizers
$4.00 Crestvane Bloody Marys
$5.00 3 - topping pizza

Mondays:
$2.00 Well Margaritas
$3.00 7 Ferns Vodka Bombs
$4.00 Rum Runners
$6.00 Philly Cheese Steak Sandwich served with loaded fries

Tuesdays:
$2.00 Meadow Fizz
$3.00 Gray Lynx
$3.00 Loaded Nachos
$3.00 Loaded Fries
$4.00 Liquid Marijuana's

Wednesdays:
$2.00 Quiet Hollow Bottles
$3.00 Blue Stars
$3.00 Zingo Rods
$4.00 Bartender Bombs
$4.00 2 Topping Pizzas

Thursdays:
~*~*Ladies Night Thursday*~
$3.00 Tart Crumb
$3.00 Sweet Affair
$3 1/2 dozen wings!
$4.00 Spin Doctors
LADIES ONLY SPECIALS
$2.00 7 Ferns Shots
$3.00 Long Islands
$4.00 Bartender Bombs!

Fridays:
$2.00 Tavu Melora Pineapple Beer
$2.00 Lumbermill ale
$2.00 Brisk Kettle
$2.00 Wandering Pike
$3.00 Little Beers
$3.00 banana pepper rings...
$3.00 hot pepper cheese balls
$4.00 Washington Apples

Saturdays:
Extended Happy Hour (12-8)
$1.00 Domestic Drafts
$2.00 Wine Coolers
$2.00 Lumbermill Ale
$2.00 Gorbys Hard Iced Tea
$3.00 Sweet Affair
$3.00 Irish Breakfast Shots
$4.00 Irish Car Bombs
$4.00 Nova Drops
~*Until 8PM*~

add some tear off coupons that I can edit dollars and offers:
$2.00 off Pizza
$2.00 Philly Cheese Steak
Contact for us for birthday party discounts and fund raising events

attached is our company logo

I also attached a flyer of something I liked I picked up

Reason: great designs.. I need to digest them

Reason: Out of town

```html
<!DOCTYPE html>
<html lang="en">
<head>
<meta charset="utf-8">
<title>Tumble Tap Weekly Specials</title>
<link rel="stylesheet" href="https://fonts.googleapis.com/css2?family=Arvo:wght@400;700&family=Tinos:wght@400;700&display=swap">
<style>
  :root {
    --red-deep: #9b1418;
    --red-bright: #d9301f;
    --paper: #ffffff;
    --ink: #1c1c1c;
    --heading-red: #b3201d;
    --happy-orange: #f3b02a;
    --beer-top: #ffe45a;
    --beer-mid: #fcc419;
    --beer-low: #f6a80e;
    --footer-ink: #6b2a10;
    --footer-link: #b3201d;
    --bullet: #f3b02a;
  }
  * { box-sizing: border-box; margin: 0; padding: 0; }
  html, body { width: 848px; height: 1200px; overflow: hidden; }
  body { position: relative; font-family: "Tinos", "Times New Roman", serif; color: var(--ink); }

  .flyer {
    position: relative; width: 848px; height: 1200px; overflow: hidden;
    background: radial-gradient(ellipse at 50% 55%, var(--red-bright) 0%, #c22219 45%, var(--red-deep) 100%);
  }
  .paper {
    position: absolute; left: 57px; top: 57px; width: 734px; height: 1143px;
    background: var(--paper);
  }
  .beer { position: absolute; left: 0; top: 0; width: 848px; height: 1200px; }

  .brand {
    position: absolute; left: 0; width: 848px; top: 138px; text-align: center;
    font-family: "Arvo", Georgia, serif; font-weight: 700; font-size: 46px;
    letter-spacing: 1px; color: var(--ink);
  }
  .promo {
    position: absolute; left: 111px; top: 250px; font-size: 20px; white-space: nowrap;
  }
  .promo .price {
    font-family: "Arvo", Georgia, serif; font-weight: 700; font-size: 30px;
    color: var(--heading-red); margin-right: 14px; vertical-align: -3px;
  }
  .happy-title {
    position: absolute; left: 0; width: 848px; top: 298px; text-align: center;
    font-family: "Arvo", Georgia, serif; font-size: 48px; color: var(--happy-orange);
  }
  .happy-hours {
    position: absolute; left: 0; width: 848px; top: 356px; text-align: center;
    font-size: 21px; letter-spacing: 0.5px;
  }

  .day { position: absolute; }
  .day h2 {
    font-family: "Arvo", Georgia, serif; font-weight: 700; font-size: 32px;
    color: var(--heading-red); line-height: 38px;
  }
  .day ul { list-style: none; }
  .day li { font-weight: 700; font-size: 14px; line-height: 19.5px; white-space: nowrap; }
  .day li.gap { height: 19.5px; }
  .day li.ladies { color: var(--heading-red); font-weight: 400; font-size: 14.5px; }
  .day li.dot::before {
    content: ""; display: inline-block; width: 7px; height: 7px; border-radius: 50%;
    background: var(--bullet); margin-right: 3px; vertical-align: 1px;
  }
  .day .indent { padding-left: 6px; }

  .sundays { left: 81px; top: 418px; }
  .mondays { left: 81px; top: 594px; }
  .tuesdays { left: 81px; top: 751px; }
  .wednesdays { left: 338px; top: 418px; }
  .thursdays { left: 338px; top: 597px; }
  .fridays { left: 567px; top: 414px; }
  .saturdays { left: 567px; top: 628px; }

  .footer {
    position: absolute; left: 0; width: 848px; top: 1134px; text-align: center;
    font-size: 15px; line-height: 22px; color: var(--footer-ink);
  }
  .footer .social { color: var(--footer-link); }
</style>
</head>
<body>
<div class="flyer">
  <div class="paper"></div>

  <svg class="beer" viewBox="0 0 848 1200" role="img" aria-label="Golden beer with foam and bubbles rising across the bottom of the flyer">
    <defs>
      <linearGradient id="beerFill" x1="0" y1="0" x2="0" y2="1">
        <stop offset="0" stop-color="#fff6c8"/>
        <stop offset="0.12" stop-color="var(--beer-top)"/>
        <stop offset="0.55" stop-color="var(--beer-mid)"/>
        <stop offset="1" stop-color="var(--beer-low)"/>
      </linearGradient>
    </defs>
    <path d="M0 840 C120 850 190 905 300 915 C400 925 470 905 560 880 C650 855 740 830 848 822 L848 1200 L0 1200 Z" fill="url(#beerFill)"/>
  </svg>

  <div class="brand">TUMBLE TAP</div>

  <p class="promo"><span class="price">$1.00</span>Domestic Drafts every day during happy hour</p>
  <h1 class="happy-title">Happy hour hours</h1>
  <p class="happy-hours">Mon-Fri 3-7 Sat &amp; Sun 12-7</p>

  <section class="day sundays">
    <h2>Sundays</h2>
    <ul>
      <li>Free Pool ALL day on both tables</li>
      <li>$1.00 Domestic drafts until midnight</li>
      <li class="gap"></li>
      <li>$3.00 Appetizers</li>
      <li>$4.00 Crestvane Bloody Marys</li>
      <li>$5.00 3 - topping pizza</li>
    </ul>
  </section>

  <section class="day mondays">
    <h2>Mondays</h2>
    <ul>
      <li>$2.00 Well Margaritas</li>
      <li>$3.00 7 Ferns Vodka Bombs</li>
      <li>$4.00 Rum Runners</li>
      <li>$6.00 Philly Cheese Steak</li>
      <li>Sandwich served with loaded fries</li>
    </ul>
  </section>

  <section class="day tuesdays">
    <h2>Tuesdays</h2>
    <ul>
      <li>$2.00 Meadow Fizz</li>
      <li>$3.00 Gray Lynx</li>
      <li>$3.00 Loaded Nachos</li>
      <li>$3.00 Loaded Fries</li>
      <li>$4.00 Liquid Marijuana's</li>
    </ul>
  </section>

  <section class="day wednesdays">
    <h2>Wednesdays</h2>
    <ul>
      <li>$2.00 Quiet Hollow Bottles</li>
      <li>$3.00 Blue Stars</li>
      <li>$3.00 Zingo Rods</li>
      <li>$4.00 Bartender Bombs</li>
      <li>$4.00 2 Topping Pizzas</li>
    </ul>
  </section>

  <section class="day thursdays">
    <h2>Thursdays</h2>
    <ul>
      <li class="indent">Ladies Night Thursday</li>
      <li>$3.00 Tart Crumb</li>
      <li>$3.00 Sweet Affair</li>
      <li>$3 1/2 dozen wings!</li>
      <li>$4.00 Spin Doctors</li>
      <li class="ladies">LADIES ONLY SPECIALS</li>
      <li class="dot">$2.00 7 Ferns Shots</li>
      <li class="dot">$3.00 Long Islands</li>
      <li class="dot">$4.00 Bartender Bombs!</li>
    </ul>
  </section>

  <section class="day fridays">
    <h2>Fridays</h2>
    <ul>
      <li>$2.00 Tavu Melora Pineapple Beer</li>
      <li>$2.00 Lumbermill ale</li>
      <li>$2.00 Brisk Kettle</li>
      <li>$2.00 Wandering Pike</li>
      <li>$3.00 Little Beers</li>
      <li>$3.00 banana pepper rings...</li>
      <li>$3.00 hot pepper cheese balls</li>
      <li>$4.00 Washington Apples</li>
    </ul>
  </section>

  <section class="day saturdays">
    <h2>Saturdays</h2>
    <ul>
      <li>Extended Happy Hour (12-8)</li>
      <li>$1.00 Domestic Drafts</li>
      <li>$2.00 Wine Coolers</li>
      <li>$2.00 Lumbermill Ale</li>
      <li>$2.00 Gorbys Hard Iced Tea</li>
      <li>$3.00 Sweet Affair</li>
      <li>$3.00 Irish Breakfast Shots</li>
      <li>$4.00 Irish Car Bombs</li>
      <li>$4.00 Nova Drops</li>
    </ul>
  </section>

  <footer class="footer">
    <p>518 Birchgrove Lane: Wellington, Ohio 57129</p>
    <p class="social">Join Us on Pagewave \Tumbletap</p>
  </footer>
</div>
</body>
</html>
```